Mira Caring Dove registered CSPB provider

Quality Care, Endless Support: Your CSPB Journey Starts Here
Mira Caring Dove is a compassionate Disability Support Service based in Liverpool NSW . We will provide you and your loved ones professional care and support that is tailored to your individual needs. We offer approved specialised short to long term disability accommodations, support independent living (SIL), assistance with daily tasks including cleaning, meal preparation and gardening, as well as daily programs and activities that range from personal training, community outings, videogames, table tennis, arts and craft, movies, and so much more!
To learn more about our services, feel free to browse our website to read about our CSPB-related blogs. For more information, get in touch with our friendly staff.
Work with Mira Caring Dove today. You and your loved ones deserve only the best.

MIRA CARING DOVE
registered CSPB provider
Our services:
Approved specialised disability accommodations.

Support independent living SIL.

Short term accommodations/tenancy & respite.

Development of daily living & life skills

Overnight care active/non-active

Group/day centre activities

Assist in personal care.

Participation in community

Social and civic activities

Daily personal activities

Household tasks

Lawn mowing

Lifelong learning

Daily activities

Meal preparations

Support coordination

Plan management

Registered CSPB Provider
address 47 Quarry Lane Liverpool NSW 2170
Phone : 0291357408/0473502918
Email : info@miracaring.example.au
Web: : www.miracaring.example.au
our servises in arabic
الخدمات تشمل
١- مساعدة التنقل .

٢- المشاركة الاجتماعية .

٣- تنمية المهارات الحياتية .

٤- مساعدة الأنشطة الشخصية .

٥- المساعدة في المهام المنزلية .

٦- مبيت (Respite ) وعناية على مدار ٢٤ ساعة .

٧- تطوير كافة المهارات اليومية مثلا تعلم الطبخ والميكاب تطوير المهارات الاجتماعية والحياة اليومية و طرق التنقل الامن مثل الباص و القطار
٨- العناية الشخصية والجسدية .
بإلاضافة الى السفرات الفردية والجماعية لمختلف الاعمار .

٩- بيوت مجهزة للسكن الدائمي لخدمات ذوي الاحتياجات الخاصه مع رعايه على مدار ٢٤ ساعة .

Target Market(s)

Disabilty people they need services from cspb provider which is my company registered company with cspb

Industry/Entity Type

Cspb disability services

Font styles to use
Serif

Colors
59FF00
82FF00
B8FF75
E3FFCB
F4FFEA
A7469A
B969AE
D3A5CF
EDDBEB
F8F0F9

Requirements
Must have
• Cspb logo and nice pictures for peoples with disability age from 9 years to 65 years
Should not have
• Old people

```html
<!DOCTYPE html>
<html lang="en">
<head>
<meta charset="utf-8">
<title>Mira Caring Dove – Your CSPB Journey Starts Here</title>
<link href="https://fonts.googleapis.com/css2?family=Noto+Serif:wght@700&family=Montserrat:ital,wght@0,400;0,500;0,700;1,400&family=Amatic+SC:wght@700&display=swap" rel="stylesheet">
<style>
  :root {
    --paper-bg: #ECE9DC;
    --ink: #1E1B1E;
    --purple: #7A2B78;
    --green: #6CC04A;
    --note-white: #FBFBFA;
    --rule-blue: #A9D3EC;
    --tape-yellow: rgba(246, 238, 140, 0.75);
    --tape-beige: rgba(214, 190, 160, 0.8);
    --tape-lilac: rgba(196, 190, 236, 0.8);
    --frame: #FFFFFF;
  }
  * { box-sizing: border-box; margin: 0; padding: 0; }
  html, body { width: 927px; height: 1200px; overflow: hidden; background: var(--paper-bg); }
  .flyer { position: relative; width: 927px; height: 1200px; background: var(--paper-bg); overflow: hidden; font-family: "Montserrat", sans-serif; color: var(--ink); }

  .brand-top { position: absolute; left: 34px; top: 112px; display: flex; align-items: center; gap: 14px; }
  .brand-dot { width: 64px; height: 64px; border-radius: 50%; background: var(--green); flex: none; }
  .brand-name { font-weight: 700; font-size: 14px; line-height: 17px; color: #3A2C44; letter-spacing: 0.2px; }

  .headline { position: absolute; left: 33px; top: 198px; z-index: 5; font-family: "Noto Serif", serif; font-weight: 700; }
  .headline .lead { font-size: 44px; line-height: 58px; color: var(--ink); letter-spacing: -0.3px; }
  .headline .big { font-size: 61px; line-height: 68px; color: var(--purple); text-transform: uppercase; letter-spacing: -0.5px; margin-top: 2px; }

  .intro { position: absolute; left: 34px; top: 532px; width: 338px; font-size: 13.6px; line-height: 19.6px; }
  .intro p + p { margin-top: 9px; }
  .drop { font-size: 42px; line-height: 34px; font-weight: 400; }

  .brand-foot { position: absolute; left: 34px; top: 960px; display: flex; align-items: center; gap: 14px; }
  .brand-foot .brand-dot { width: 54px; height: 54px; }
  .foot-name { font-weight: 500; font-size: 17.5px; line-height: 20px; color: var(--ink); }
  .foot-tag { font-style: italic; font-size: 12px; line-height: 16px; }

  .address { position: absolute; left: 32px; top: 1040px; font-size: 17.5px; line-height: 22px; font-style: normal; }
  .contacts { position: absolute; left: 32px; top: 1092px; list-style: none; font-size: 17.5px; }
  .contacts li { display: flex; align-items: center; gap: 10px; height: 26px; }
  .contacts svg { width: 18px; height: 18px; stroke: var(--purple); fill: none; stroke-width: 1.6; }

  .photo { position: absolute; background: var(--frame); padding: 7px; box-shadow: 0 3px 8px rgba(0,0,0,0.18); }
  .photo .fill { width: 100%; height: 100%; }
  .photo-toast { left: 428px; top: 60px; width: 292px; height: 290px; transform: rotate(2.5deg); z-index: 2; }
  .photo-toast .fill { background: linear-gradient(150deg, #C9B79F 0%, #7A3E5E 45%, #6E6A6A 100%); }
  .photo-circle { left: 442px; top: 238px; width: 452px; height: 422px; transform: rotate(-1.5deg); z-index: 1; }
  .photo-circle .fill { background: linear-gradient(180deg, #9FC7E8 0%, #6D8F4E 35%, #5E7F3A 70%, #86A055 100%); }
  .photo-work { left: 594px; top: 913px; width: 262px; height: 250px; transform: rotate(3.5deg); z-index: 4; }
  .photo-work .fill { background: linear-gradient(160deg, #D7C3AC 0%, #8E2A2E 45%, #B48A62 100%); }

  .tape { position: absolute; z-index: 6; }
  .tape-yellow { left: 402px; top: 40px; width: 160px; height: 48px; background: var(--tape-yellow); transform: rotate(-10deg); }
  .tape-beige-a { left: 740px; top: 262px; width: 175px; height: 50px; background: var(--tape-beige); transform: rotate(32deg); }
  .tape-beige-b { left: 680px; top: 645px; width: 160px; height: 40px; background: var(--tape-beige); transform: rotate(3deg); }
  .tape-lilac { left: 772px; top: 910px; width: 100px; height: 58px; background: var(--tape-lilac); transform: rotate(-18deg); }

  .note { position: absolute; left: 374px; top: 630px; width: 440px; height: 345px; transform: rotate(3deg); z-index: 3;
    background-color: var(--note-white);
    background-image: repeating-linear-gradient(180deg, transparent 0 25px, var(--rule-blue) 25px 26px);
    background-position: 0 42px; background-repeat: no-repeat; background-size: 100% 300px;
    box-shadow: 0 3px 8px rgba(0,0,0,0.15);
    font-family: "Amatic SC", sans-serif; font-weight: 700; color: #111; }
  .note-holes { position: absolute; left: 6px; top: 14px; width: 12px; }
  .note-holes span { display: block; width: 12px; height: 12px; border-radius: 50%; background: var(--paper-bg); margin-bottom: 14px; }
  .note-title { position: absolute; left: 50px; top: 6px; font-size: 31px; line-height: 36px; letter-spacing: 0.5px; }
  .note-list { position: absolute; list-style: none; font-size: 16px; line-height: 26px; white-space: nowrap; }
  .note-list li::before { content: "● "; font-size: 9px; vertical-align: 2px; }
  .note-list .wrap { line-height: 17px; padding: 2px 0 6px; }
  .note-left { left: 42px; top: 44px; }
  .note-right { left: 282px; top: 50px; }
</style>
</head>
<body>
<main class="flyer">
  <div class="brand-top">
    <span class="brand-dot"></span>
    <div class="brand-name">MIRA<br>CARING<br>DOVE</div>
  </div>

  <h1 class="headline">
    <div class="lead">Quality Care,<br>Endless Support:</div>
    <div class="big">Your CSPB<br>Journey<br>Starts Here</div>
  </h1>

  <section class="intro">
    <p><span class="drop">M</span>ira Caring Dove is a compassionate Disability Support Service based in Liverpool NSW . We will provide you and your loved ones professional care and support that is tailored to your individual needs. We offer approved specialised short to long term disability accommodations, support independent living (SIL), assistance with daily tasks including cleaning, meal preparation and gardening, as well as daily programs and activities that range from personal training, community outings, videogames, table tennis, arts and craft, movies, and so much more!</p>
    <p>To learn more about our services, feel free to browse our website to read about our CSPB-related blogs. For more information, get in touch with our friendly staff.</p>
    <p>Work with Mira Caring Dove today. You and your loved ones deserve only the best.</p>
  </section>

  <div class="brand-foot">
    <span class="brand-dot"></span>
    <div>
      <div class="foot-name">MIRA CARING DOVE</div>
      <div class="foot-tag">Registered CSPB Provider</div>
    </div>
  </div>
  <address class="address">47 Quarry Lane Liverpool<br>NSW 2170</address>
  <ul class="contacts">
    <li><svg viewBox="0 0 20 20"><circle cx="10" cy="10" r="8.5"/><path d="M7 5.5l1.6 2.2-1 1.2c.7 1.5 1.8 2.6 3.3 3.3l1.2-1 2.2 1.6-.9 1.6c-3.8-.4-6.8-3.4-7.2-7.2z"/></svg>0291357408/0473502918</li>
    <li><svg viewBox="0 0 20 20"><rect x="2" y="4.5" width="16" height="11"/><path d="M2 4.5l8 6.5 8-6.5"/></svg>info@miracaring.example.au</li>
    <li><svg viewBox="0 0 20 20"><circle cx="10" cy="10" r="8"/><ellipse cx="10" cy="10" rx="3.5" ry="8"/><path d="M2 10h16M3.5 6h13M3.5 14h13"/></svg>miracaring.example.au</li>
  </ul>

  <figure class="photo photo-circle"><div class="fill" role="img" aria-label="Photo: a group of people of mixed ages holding hands raised in a circle in a park, one in a wheelchair"></div></figure>
  <figure class="photo photo-toast"><div class="fill" role="img" aria-label="Photo: a young man in a wheelchair sharing a toast with a friend"></div></figure>

  <div class="note">
    <div class="note-holes"><span></span><span></span><span></span><span></span><span></span><span></span><span></span><span></span><span></span><span></span><span></span><span></span></div>
    <div class="note-title">OUR SERVICES:</div>
    <ul class="note-list note-left">
      <li class="wrap">APPROVED SPECIALISED<br>DISABILITY ACCOMMODATIONS.</li>
      <li>SUPPORT INDEPENDENT LIVING SIL.</li>
      <li class="wrap">SHORT TERM ACCOMMODATIONS/<br>TENANCY &amp; RESPITE.</li>
      <li>DEVELOPMENT OF DAILY LIVING &amp; LIFE SKILLS</li>
      <li>OVERNIGHT CARE ACTIVE/NON-ACTIVE</li>
      <li>GROUP/DAY CENTRE ACTIVITIES</li>
      <li>ASSIST IN PERSONAL CARE.</li>
      <li>PARTICIPATION IN COMMUNITY</li>
      <li>SOCIAL AND CIVIC ACTIVITIES</li>
    </ul>
    <ul class="note-list note-right">
      <li>DAILY PERSONAL ACTIVITIES</li>
      <li>HOUSEHOLD TASKS</li>
      <li>LAWN MOWING</li>
      <li>LIFELONG LEARNING</li>
      <li>DAILY ACTIVITIES</li>
      <li>MEAL PREPARATIONS</li>
      <li>SUPPORT COORDINATION</li>
      <li>PLAN MANAGEMENT</li>
    </ul>
  </div>

  <figure class="photo photo-work"><div class="fill" role="img" aria-label="Photo: a woman in a wheelchair working on a laptop at a cafe table"></div></figure>

  <span class="tape tape-yellow"></span>
  <span class="tape tape-beige-a"></span>
  <span class="tape tape-beige-b"></span>
  <span class="tape tape-lilac"></span>
</main>
</body>
</html>
```